Industrial Automation company requires a business card design

Dravik Automation provides design & build of Automated Equipment for manufacturing industry.
www.dravikautomation-example.com
The equipment we design is used for manufacturing in sectors such as medical device, pharmaceutical, aerospace and electronics.
We require a new business card design which incorporates our (New) logo and the key message words:
Automated Equipment:
Design, Build, Control, Test, Support

Industry/Entity Type

Business

```html
<!DOCTYPE html>
<html lang="en">
<head>
<meta charset="utf-8">
<title>Dravik Automation – Business Card</title>
<link href="https://fonts.googleapis.com/css2?family=Noto+Sans:wght@400;600&display=swap" rel="stylesheet">
<style>
  :root {
    --backdrop: #4a423d;
    --card: #1c1c1c;
    --green: #2f8a3e;
    --white: #f2f2f2;
    --grey: #bdbdbd;
    --divider: #6a6a6a;
  }
  * { margin: 0; padding: 0; box-sizing: border-box; }
  html, body { width: 1200px; height: 787px; overflow: hidden; }
  body {
    background: var(--backdrop);
    font-family: "Noto Sans", Verdana, sans-serif;
    position: relative;
  }
  .card {
    position: absolute;
    top: 238px;
    width: 540px;
    height: 309px;
    background: var(--card);
    border-radius: 4px;
    box-shadow: 0 8px 24px rgba(0,0,0,.45);
    overflow: hidden;
  }
  .card--front { left: 40px; }
  .card--back { left: 620px; }

  /* Front */
  .front-brand {
    position: absolute;
    left: 48px; top: 76px;
    display: flex; align-items: center; gap: 14px;
  }
  .front-brand__mark {
    width: 34px; height: 34px; border-radius: 50%;
    background: var(--green);
  }
  .front-brand__name {
    color: var(--white);
    font-size: 30px; font-weight: 600; letter-spacing: 1px;
  }
  .tagline {
    position: absolute; left: 48px; top: 168px;
    color: var(--green);
    font-size: 21px; font-weight: 400;
  }
  .services {
    position: absolute; left: 48px; top: 206px;
    color: var(--white); font-size: 17px;
    display: flex; gap: 10px; align-items: center;
  }
  .services .dot { color: var(--green); font-size: 14px; }

  /* Back */
  .back-brand {
    position: absolute; left: 28px; top: 138px;
    width: 205px;
    color: var(--white);
    font-size: 20px; font-weight: 600; letter-spacing: .4px;
    line-height: 1.25;
    white-space: nowrap;
  }
  .divider {
    position: absolute; left: 246px; top: 40px;
    width: 1px; height: 230px;
    background: var(--divider);
  }
  .contact {
    position: absolute; left: 262px; top: 40px; right: 16px;
    color: var(--white); font-size: 12px; line-height: 1.5;
  }
  .contact__name { color: var(--green); font-size: 18px; font-weight: 600; line-height: 1.2; }
  .contact__role { font-size: 14px; margin-bottom: 12px; }
  .contact__address { margin-bottom: 14px; }
  .contact__row { display: flex; align-items: center; gap: 8px; white-space: nowrap; }
  .contact__row svg { width: 12px; height: 12px; flex: none; fill: var(--green); }
</style>
</head>
<body>

<section class="card card--front">
  <div class="front-brand">
    <span class="front-brand__mark"></span>
    <span class="front-brand__name">Dravik Automation</span>
  </div>
  <p class="tagline">Automated Equipment</p>
  <p class="services">
    <span>Design</span><span class="dot">●</span>
    <span>Build</span><span class="dot">●</span>
    <span>Control</span><span class="dot">●</span>
    <span>Test</span><span class="dot">●</span>
    <span>Support</span>
  </p>
</section>

<section class="card card--back">
  <div class="back-brand">Dravik Automation</div>
  <div class="divider"></div>
  <div class="contact">
    <p class="contact__name">Marlen Oskar</p>
    <p class="contact__role">President</p>
    <p class="contact__address">4127 Alder Crest Road<br>Brookvale, NY 11920</p>
    <p class="contact__row">
      <svg viewBox="0 0 16 16" aria-hidden="true"><path d="M3 1h3l1.5 4-2 1.2a9 9 0 0 0 4.3 4.3L11 8.5l4 1.5v3a2 2 0 0 1-2 2A13 13 0 0 1 1 3a2 2 0 0 1 2-2z"/></svg>
      555 0142 7781
    </p>
    <p class="contact__row">
      <svg viewBox="0 0 16 16" aria-hidden="true"><path d="M4 0h8a1 1 0 0 1 1 1v14a1 1 0 0 1-1 1H4a1 1 0 0 1-1-1V1a1 1 0 0 1 1-1zm1 2v10h6V2zm3 11a1 1 0 1 0 0 2 1 1 0 0 0 0-2z"/></svg>
      555 0198 3364
    </p>
    <p class="contact__row">
      <svg viewBox="0 0 16 16" aria-hidden="true"><path d="M1 3h14v10H1zm1.5 1.2V12h11V4.2L8 8.5z"/></svg>
      marlen@dravikautomation-example.com
    </p>
    <p class="contact__row">
      <svg viewBox="0 0 16 16" aria-hidden="true"><circle cx="8" cy="8" r="7"/><path d="M1 8h14M8 1c3 3 3 11 0 14M8 1c-3 3-3 11 0 14" stroke="#1c1c1c" stroke-width="1" fill="none"/></svg>
      www.dravikautomation-example.com
    </p>
  </div>
</section>

</body>
</html>
```